K7 seamless

We are a glazing company specializing in frameless glass .
I would like the business cards in black with the logo taking up the most part of the front added with " frameless glass specialist's " below it.
On the back side I would like a list of what we do :
• shower screens
• glass balustrade / pool fencing
• mirrors
•office partitions
• sky lights
•shop fronts
•splash backs
Also include this information :
📧 - corbin@k7seamless.com
📞Corbin - 0418276594
📞 Milo - 0427 613 508
Updates
To all designs already posted can you include on the back of the card in the services part -
•splash backs
Target Market(s)
High end builders
Industry/Entity Type
Glazing
Contact Information for Business Card
On the back side I would like a list of what we do : • shower screens • glass balustrade / pool fencing • mirrors •office partitions • sky lights •shop fronts Also include this information : 📧 - corbin@k7seamless.com 📞Corbin - 0418276594 📞 Milo - 0427 613 508
Colors
Designer to choose colors to be used in the design.
Look and feel
Each slider illustrates characteristics of the customer's brand and the style your logo design should communicate.

```html
<!DOCTYPE html>
<html lang="en">
<head>
<meta charset="utf-8">
<title>K7 seamless – Business Cards</title>
<link href="https://fonts.googleapis.com/css2?family=Open+Sans:wght@400;600;700&display=swap" rel="stylesheet">
<style>
  :root {
    --backdrop: #242424;
    --card: #1e1e22;
    --white: #ffffff;
    --teal: #2fb79b;
    --teal-bright: #14b8c4;
    --muted: #d9d9d9;
  }
  * { box-sizing: border-box; margin: 0; padding: 0; }
  html, body {
    width: 1200px; height: 780px; overflow: hidden;
    background: var(--backdrop);
    font-family: "Open Sans", Arial, sans-serif;
  }
  .sheet {
    width: 1200px; height: 780px;
    display: flex; align-items: center; justify-content: center; gap: 40px;
  }
  .card {
    position: relative;
    width: 540px; height: 310px;
    background: var(--card);
    box-shadow: 0 18px 40px rgba(0,0,0,.45);
  }
  .brand {
    display: flex; align-items: center; gap: 12px;
    color: var(--white); font-weight: 700; letter-spacing: .5px;
    white-space: nowrap;
  }
  .brand-square { background: var(--teal); flex: none; }

  /* Contact side */
  .card-contact .brand {
    position: absolute; left: 40px; top: 128px; font-size: 30px;
  }
  .card-contact .brand-square { width: 18px; height: 18px; }
  .divider {
    position: absolute; left: 268px; top: 95px;
    width: 1px; height: 120px; background: var(--white); opacity: .85;
  }
  .contacts {
    position: absolute; left: 296px; top: 110px;
    list-style: none; display: flex; flex-direction: column; gap: 12px;
  }
  .contact {
    display: flex; align-items: center; gap: 10px;
    color: var(--white); font-size: 15.5px; font-weight: 600;
  }
  .contact svg { width: 16px; height: 16px; flex: none; }
  .contact-name { color: var(--teal); font-weight: 700; font-size: 17px; }

  /* Services side */
  .card-services .brand {
    position: absolute; left: 0; right: 0; top: 74px;
    justify-content: center; font-size: 40px;
  }
  .card-services .brand-square { width: 24px; height: 24px; }
  .services-title {
    position: absolute; left: 0; right: 0; top: 160px;
    text-align: center; color: var(--teal-bright);
    font-size: 13px; font-weight: 400; letter-spacing: 1px;
  }
  .services {
    position: absolute; left: 30px; right: 30px; top: 188px;
    text-align: center; color: var(--muted);
    font-size: 11.5px; letter-spacing: .4px; line-height: 1.9;
    text-transform: uppercase;
  }
  .services-row { display: block; }
  .dot {
    display: inline-block; width: 6px; height: 6px; border-radius: 50%;
    background: var(--teal); margin: 0 7px; vertical-align: middle;
  }
</style>
</head>
<body>
<main class="sheet">
  <section class="card card-contact" aria-label="Business card – contact side">
    <div class="brand"><span class="brand-square"></span>K7 seamless</div>
    <div class="divider"></div>
    <ul class="contacts">
      <li class="contact">
        <svg viewBox="0 0 24 24" aria-hidden="true"><path fill="var(--teal)" d="M6.6 10.8a15.1 15.1 0 0 0 6.6 6.6l2.2-2.2a1 1 0 0 1 1-.25 11.4 11.4 0 0 0 3.6.57 1 1 0 0 1 1 1V20a1 1 0 0 1-1 1A17 17 0 0 1 3 4a1 1 0 0 1 1-1h3.5a1 1 0 0 1 1 1c0 1.25.2 2.46.57 3.6a1 1 0 0 1-.25 1z"/></svg>
        <span>0418276594 - <span class="contact-name">Corbin</span></span>
      </li>
      <li class="contact">
        <svg viewBox="0 0 24 24" aria-hidden="true"><path fill="var(--teal)" d="M6.6 10.8a15.1 15.1 0 0 0 6.6 6.6l2.2-2.2a1 1 0 0 1 1-.25 11.4 11.4 0 0 0 3.6.57 1 1 0 0 1 1 1V20a1 1 0 0 1-1 1A17 17 0 0 1 3 4a1 1 0 0 1 1-1h3.5a1 1 0 0 1 1 1c0 1.25.2 2.46.57 3.6a1 1 0 0 1-.25 1z"/></svg>
        <span>0427 613 508 - <span class="contact-name">Milo</span></span>
      </li>
      <li class="contact">
        <svg viewBox="0 0 24 24" aria-hidden="true"><rect x="2" y="5" width="20" height="14" rx="2" fill="var(--teal)"/><path d="M3 6l9 7 9-7" fill="none" stroke="var(--card)" stroke-width="1.8"/></svg>
        <span>corbin@k7seamless.com</span>
      </li>
    </ul>
  </section>

  <section class="card card-services" aria-label="Business card – services side">
    <div class="brand"><span class="brand-square"></span>K7 seamless</div>
    <h2 class="services-title">WHAT WE DO</h2>
    <p class="services">
      <span class="services-row">Shower Screens<span class="dot"></span>Glass Balustrade / Pool Fencing<span class="dot"></span>Mirrors</span>
      <span class="services-row">Office Partitions<span class="dot"></span>Sky Lights<span class="dot"></span>Shop Fronts<span class="dot"></span>Splash Backs</span>
    </p>
  </section>
</main>
</body>
</html>
```